Brochure Design Project

We need a brochure to introduce clients who work in our local area to become a VIP clients based on the fact they work in the local area. We have call centers of major companies with 1 km of our hair salon as well as head offices of many big companies some with staff of 400 and Australia second biggest University Carrowby with 1500 international student who live mins away who use our local shops to have lunch as we have many food outlets we have a wide mix of people walking past our salon at lunch time demographic ages from 19yo call center staff to CEO's. I not sure whether to use VIP what are your thoughts and statistics say (overuse). I need your thoughts on how they would qualify to become a VIP i was thinking they only need to show proof they work in one of the offices in our area to become a member I will provide them with a small plastic bar coded tag to identify themselves if they become members you can profile our business from our website www.vessoria.com.au our NEW logo is on our facebook page Vessoria Hair and Make up web logo is the old one I think we should put in our price list which is on our website i was thinking 20% off normal prices subject to change.

Reason: I need more time to organize staff

Target Market(s)

Local traders and local offices we have many call centre staff and big company head offices with in 1 km

Industry/Entity Type

Plastic

Requirements
Must have
• Simplicity not too busy less is more
Nice to have
• A4 Folded
Should not have
• Too much text

```html
<!DOCTYPE html>
<html lang="en">
<head>
<meta charset="utf-8">
<title>Vessoria – About Us &amp; Price List</title>
<link href="https://fonts.googleapis.com/css2?family=Gilda+Display&family=Tinos:wght@400&display=swap" rel="stylesheet">
<style>
:root{
  --orange:#f07a1f;
  --ink:#1d1d1d;
  --bar:#222222;
  --paper:#ffffff;
}
*{margin:0;padding:0;box-sizing:border-box}
html,body{width:1200px;height:844px;overflow:hidden;background:var(--paper)}
.brochure{position:relative;width:1200px;height:844px;font-family:"Tinos","Times New Roman",serif;color:var(--ink);overflow:hidden}
.display{font-family:"Gilda Display","Times New Roman",serif;font-weight:400}
.abs{position:absolute}

/* About panel */
.about-title{left:26px;top:20px;font-size:66px;letter-spacing:-1px;line-height:1}
.about-band{left:0;top:132px;width:400px;height:484px;background:var(--orange)}
.about-lines{left:0;top:118px}
.model-photo{left:0;top:370px;width:310px;height:474px;
  background:linear-gradient(160deg,#e6e6e6 0%,#b5b5b5 35%,#7d7d7d 70%,#5a5a5a 100%);
  clip-path:polygon(0 10px,60px 2px,140px 20px,150px 100px,205px 130px,210px 220px,300px 250px,310px 474px,0 474px);}
.about-copy{left:40px;top:152px;width:320px;color:var(--paper);font-size:15.5px;line-height:20.5px}
.about-copy p{margin-bottom:20.5px}
.line{display:block;white-space:nowrap;text-align:justify;text-align-last:justify}
.about-accolades{left:140px;top:398px;width:220px;color:var(--paper);font-size:15.5px;line-height:20.5px;text-align:right}

/* Price list header */
.price-brush{left:432px;top:0}
.price-title{left:562px;top:18px;font-size:68px;color:var(--paper);line-height:1;letter-spacing:-1px}
.price-title .accent{color:var(--orange);margin-left:62px}

/* Sections */
.bar{height:18px;background:var(--bar);color:var(--paper);font-size:14px;line-height:18px;text-align:center;letter-spacing:.3px}
.bar--accent{color:var(--orange)}
.col-mid{left:440px;width:320px}
.col-right{left:840px;width:320px}
.blurb{font-size:11px;line-height:14.5px;text-align:justify;text-align-last:center}
.note{font-size:11px;line-height:14px}
.accent{color:var(--orange)}
.table .row{display:grid;height:20px;line-height:20px;font-size:11.5px;text-align:center}
.cuts .row{grid-template-columns:96px 130px 94px}
.blow .row{grid-template-columns:108px 114px 98px}
.colours .row{grid-template-columns:78px 124px 118px}
.foil .row{grid-template-columns:96px 128px 96px;height:21px;line-height:21px;font-size:12.5px}
.foilcol .row{grid-template-columns:70px 120px 130px}
.ammonia{font-size:10px;color:var(--orange)}
.conditions{font-size:12.5px;line-height:18px;text-align:center}
.contact-lines{left:800px;top:692px}
.contact-band{left:800px;top:716px;width:400px;height:128px;background:var(--orange);color:var(--paper);text-align:center;font-size:15px;line-height:24px;padding-top:26px}
</style>
</head>
<body>
<div class="brochure">

  <!-- About -->
  <h1 class="abs about-title display">ABOUT US</h1>
  <svg class="abs about-lines" width="400" height="20" viewBox="0 0 400 20" aria-hidden="true">
    <path d="M0 4 L395 2" stroke="#f5a264" stroke-width="1"/>
    <path d="M0 8 L400 6" stroke="#f5a264" stroke-width="1.5"/>
    <path d="M0 12 L398 11" stroke="#f5a264" stroke-width="1"/>
  </svg>
  <div class="abs about-band"></div>
  <div class="abs model-photo" role="img" aria-label="Black and white portrait of a model with long flowing blonde hair"></div>
  <div class="abs about-copy">
    <p><span class="line">After nearly three decades, Vessoria is somewhat</span><span class="line">of an institution in hairdressing in Melbourne.</span></p>
    <p><span class="line">Tradition, prestige and innovation set the</span><span class="line">foundations for what the salon epitomises. It</span><span class="line">embodies a culture where technique meets</span><span class="line">creativity to produce work of the highest calibre.</span></p>
    <p><span class="line">An infusion of both modernity and opulence</span><span class="line">are the cornerstone in manifesting our</span><span class="line">lifestyle salons of style and sophistication.</span></p>
  </div>
  <p class="abs about-accolades">Vessoria is no stranger to the<br>media spotlight. With over 70<br>awards and accolades, both<br>nationally and<br>internationally, it has<br>earned an enviable<br>reputation for hair<br>excellence and<br>service quality.</p>

  <!-- Price list header -->
  <svg class="abs price-brush" width="768" height="104" viewBox="0 0 768 104" aria-hidden="true">
    <path d="M14 6 L768 0 L768 92 L600 96 L420 100 L240 98 L60 102 L20 94 L30 84 L8 76 L24 62 L4 50 L22 38 L6 26 L20 16 Z" fill="#1b1b1b"/>
    <path d="M40 98 L300 104 M320 96 L560 101" stroke="#1b1b1b" stroke-width="2"/>
  </svg>
  <h2 class="abs price-title display">PRICE<span class="accent">LIST</span></h2>

  <!-- Middle column -->
  <div class="abs col-mid bar bar--accent" style="top:123px">SERVICES</div>
  <p class="abs col-mid blurb" style="top:150px">Lumière Professionnel and Kerasol Paris are the salon's premium products of choice. A strong partnership Vessoria has shared for many years.</p>

  <div class="abs col-mid bar" style="top:203px">CUTS</div>
  <p class="abs col-mid blurb" style="top:230px">Every consultation gives careful consideration examining face shapes, features and contours. Precise intensive analysis is a reflection of our extensive in-house educational programme.</p>
  <div class="abs col-mid table cuts" style="top:283px">
    <div class="row accent"><span>Cutting</span><span>Style Director</span><span>Principal Stylist</span></div>
    <div class="row"><span>Ladies' Style Cut*</span><span>$88.00</span><span>$70.00</span></div>
    <div class="row"><span>Mens' Style Cut*</span><span>$55.00</span><span>$45.00</span></div>
  </div>
  <p class="abs col-mid note" style="top:347px;text-align:center">*Salon Director - from $90.00 (Ladies) and from $65.00 (Men)</p>

  <div class="abs col-mid bar" style="top:373px">BLOW WAVE/STYLING</div>
  <div class="abs col-mid table blow" style="top:401px">
    <div class="row"><span class="accent">Short</span><span>$50.00</span><span>$40.00</span></div>
    <div class="row"><span class="accent">Medium</span><span>$60.00</span><span>$50.00</span></div>
    <div class="row"><span class="accent">Long</span><span>$70.00</span><span>$60.00</span></div>
  </div>

  <div class="abs col-mid bar" style="top:471px">COLOURS</div>
  <p class="abs col-mid blurb" style="top:498px">Colour consultations explore a client's eye colour, skin tone, wants, needs and lifestyle . We offer directional advice, believing it is paramount in stimulating creativity for new ideas or for the refreshment of existing colour.</p>
  <div class="abs col-mid table colours" style="top:562px">
    <div class="row accent"><span>Colouring</span><span>Technical Director</span><span>Principal Colourist</span></div>
    <div class="row"><span>Regrowth</span><span>$80.00</span><span>$65.00</span></div>
    <div class="row"><span>Short</span><span>$80.00</span><span>$70.00</span></div>
    <div class="row"><span>Medium</span><span>$90.00</span><span>$80.00</span></div>
    <div class="row"><span>Long</span><span>$100.00</span><span>$90.00</span></div>
    <div class="row accent"><span>AURA *</span><span>Technical Director</span><span>Principal Colourist</span></div>
    <div class="row"><span>Regrowth</span><span>$85.00</span><span>$75.00</span></div>
    <div class="row"><span>Short</span><span>$90.00</span><span>$80.00</span></div>
    <div class="row"><span>Medium</span><span>$100.00</span><span>$95.00</span></div>
    <div class="row"><span>Long</span><span>$110.00</span><span>$110.00</span></div>
  </div>
  <p class="abs ammonia" style="left:440px;top:770px">* AMMONIA FREE</p>

  <!-- Right column -->
  <div class="abs col-right bar" style="top:123px">FOILING</div>
  <div class="abs col-right table foil" style="top:151px">
    <div class="row"><span class="accent">1/2 Head</span><span>$110.00</span><span>$85.00</span></div>
    <div class="row"><span class="accent">Full Head</span><span>$170.00</span><span>$145.00</span></div>
    <div class="row"><span class="accent">Toner</span><span>$15.00</span><span>$10.00</span></div>
  </div>

  <div class="abs col-right bar" style="top:228px">FOILING &amp; COLOUR</div>
  <div class="abs col-right table foilcol" style="top:256px">
    <div class="row accent"><span>Colouring</span><span>Technical Director</span><span>Principal Colourist</span></div>
    <div class="row"><span>Short</span><span>$125.00</span><span>$125.00</span></div>
    <div class="row"><span>Medium</span><span>$135.00</span><span>$130.00</span></div>
    <div class="row"><span>Long</span><span>$145.00</span><span>$140.00</span></div>
    <div class="row"><span>Toner</span><span>$15.00</span><span>$10.00</span></div>
    <div class="row accent"><span>AURA *</span><span>Technical Director</span><span>Principal Colourist</span></div>
    <div class="row"><span>Medium</span><span>$160.00</span><span>$145.00</span></div>
    <div class="row"><span>Long</span><span>$170.00</span><span>$160.00</span></div>
    <div class="row"><span>Toner</span><span>$15.00</span><span>$10.00</span></div>
  </div>
  <p class="abs ammonia" style="left:840px;top:446px">* AMMONIA FREE</p>

  <div class="abs col-right bar" style="top:468px">BRIDAL HAIR/FORMAL HAIR</div>
  <p class="abs col-right note" style="top:494px;text-align:center">PLease contact salon, see contact details on back.</p>
  <p class="abs col-right conditions" style="top:532px"><span class="accent">*</span>Conditions. Strictly available at Mount Arlen salon only, prices and percentage discount &amp; Vip Club Expiry subject to change with 30 days notice via In salon or email . VIP Club discounts not valid 14 working days prior to Christmas</p>

  <svg class="abs contact-lines" width="400" height="24" viewBox="0 0 400 24" aria-hidden="true">
    <path d="M0 6 L400 3" stroke="#f5a264" stroke-width="1"/>
    <path d="M4 11 L400 9" stroke="#f5a264" stroke-width="1.5"/>
    <path d="M0 16 L396 15" stroke="#f5a264" stroke-width="1"/>
  </svg>
  <div class="abs contact-band">
    <p>www.vessoria.com.au</p>
    <p>www.friendsphere.com/ vessoriahairandmakeup</p>
  </div>
</div>
</body>
</html>
```